Name of Business is Tidewell Vitality Mentor,
Business Card and Logo Design for a health coaching practice that brings together all aspects of living including breathing, meditation, heartfelt intentional living, oneness with others, compassion, nutrition, hydration and primary care physician.

Target Market(s)

People looking for holistic approach to optimal living.

Industry/Entity Type

Business

Contact Information for Business Card

Marcus R.T. Dunmore
CWM, HVC, R-BQ
Tidewell Vitality Mentor
614 Birchmoor Ave
Alderbrook Heights, MI 49307

Logo Text

Everything You Need Is Within You Now

```html
<!DOCTYPE html>
<html lang="en">
<head>
<meta charset="utf-8">
<title>Tidewell Vitality Mentor – Business Card</title>
<link href="https://fonts.googleapis.com/css2?family=Open+Sans:wght@400;600;700&display=swap" rel="stylesheet">
<style>
  :root {
    --bg: #3a3d42;
    --card-white: #ffffff;
    --brand-blue: #2a63b4;
    --deep-blue: #2c4f9e;
    --bright-blue: #1a7fd0;
    --ink: #1b1b1b;
  }
  * { margin: 0; padding: 0; box-sizing: border-box; }
  html, body { width: 1200px; height: 800px; overflow: hidden; }
  body {
    background: var(--bg);
    font-family: "Open Sans", Arial, sans-serif;
    position: relative;
  }
  .card {
    position: absolute;
    width: 600px;
    height: 343px;
    border-radius: 3px;
    overflow: hidden;
    box-shadow: 0 10px 30px rgba(0,0,0,0.35);
  }

  /* Back of card */
  .card-back {
    left: 520px; top: 40px;
    background: radial-gradient(ellipse at 45% 35%, var(--bright-blue) 0%, var(--brand-blue) 45%, var(--deep-blue) 100%);
    color: #fff;
    display: flex; flex-direction: column; align-items: center; justify-content: center;
  }
  .brand-mark {
    display: flex; flex-direction: column; align-items: center; gap: 14px;
  }
  .brand-dot {
    width: 70px; height: 70px; border-radius: 50%;
    background: #fff;
    flex: none;
  }
  .brand-name {
    font-size: 30px; font-weight: 600; letter-spacing: 0.5px; white-space: nowrap;
  }
  .card-back .brand-name { color: #fff; }
  .card-back .site {
    margin-top: 26px; font-size: 14px; letter-spacing: 1px;
  }

  /* Front of card */
  .card-front {
    left: 80px; top: 417px;
    background: var(--card-white);
  }
  .front-logo {
    position: absolute; left: 18px; top: 105px; width: 272px;
    display: flex; flex-direction: column; align-items: center; gap: 12px;
  }
  .front-logo .brand-dot {
    width: 62px; height: 62px; background: var(--brand-blue);
  }
  .front-logo .brand-name {
    color: var(--brand-blue); font-size: 19px; text-align: center;
  }
  .divider {
    position: absolute; left: 300px; top: 80px;
    width: 1.5px; height: 150px; background: var(--brand-blue);
  }
  .contact-block {
    position: absolute; left: 330px; top: 78px; color: var(--ink);
  }
  .person-name {
    color: var(--brand-blue); font-size: 21px; font-weight: 700; line-height: 1.1;
  }
  .credentials, .role { font-size: 13px; line-height: 1.35; }
  .credentials { margin-top: 6px; }
  .contact-list { list-style: none; margin-top: 12px; }
  .contact-list li {
    display: flex; align-items: center; gap: 12px;
    font-size: 14.5px; line-height: 1.45;
  }
  .contact-list svg { width: 13px; height: 13px; fill: var(--brand-blue); flex: none; }
  .address {
    position: absolute; left: 0; right: 0; top: 286px;
    text-align: center; font-size: 15px; color: var(--ink);
  }
  .base-band {
    position: absolute; left: 0; right: 0; bottom: 0; height: 9px;
    background: linear-gradient(90deg, var(--deep-blue), var(--bright-blue) 50%, var(--deep-blue));
  }
</style>
</head>
<body>

  <section class="card card-back">
    <div class="brand-mark">
      <span class="brand-dot"></span>
      <span class="brand-name">Tidewell Vitality Mentor</span>
    </div>
    <p class="site">www.tidewellvitality.com</p>
  </section>

  <section class="card card-front">
    <div class="front-logo">
      <span class="brand-dot"></span>
      <span class="brand-name">Tidewell Vitality Mentor</span>
    </div>

    <div class="divider"></div>

    <div class="contact-block">
      <h1 class="person-name">Marcus R.T. Dunmore</h1>
      <p class="credentials">CWM, HVC, R-BQ</p>
      <p class="role">Tidewell Vitality Mentor</p>
      <ul class="contact-list">
        <li>
          <svg viewBox="0 0 24 24" aria-hidden="true"><path d="M6.6 10.8a15 15 0 0 0 6.6 6.6l2.2-2.2c.3-.3.7-.4 1-.2 1.1.4 2.3.6 3.6.6.6 0 1 .4 1 1V20c0 .6-.4 1-1 1A17 17 0 0 1 3 4c0-.6.4-1 1-1h3.5c.6 0 1 .4 1 1 0 1.3.2 2.5.6 3.6.1.3 0 .7-.2 1z"/></svg>
          313 555 0142
        </li>
        <li>
          <svg viewBox="0 0 24 24" aria-hidden="true"><path d="M6 2h12v5H6zM4 8h16a2 2 0 0 1 2 2v7h-4v5H6v-5H2v-7a2 2 0 0 1 2-2zm4 8v4h8v-4z"/></svg>
          313 555 0143
        </li>
        <li>
          <svg viewBox="0 0 24 24" aria-hidden="true"><path d="M2 5h20v14H2zm2 2v.4l8 5.2 8-5.2V7zm0 2.8V17h16V9.8l-8 5.2z"/></svg>
          info@tidewellvitality.com
        </li>
        <li>
          <svg viewBox="0 0 24 24" aria-hidden="true"><path d="M12 2a10 10 0 1 0 0 20 10 10 0 0 0 0-20zm6.9 6h-3a15 15 0 0 0-1.3-4A8 8 0 0 1 18.9 8zM12 4c.9 1.2 1.6 2.6 2 4h-4c.4-1.4 1.1-2.8 2-4zM4.3 14a8 8 0 0 1 0-4h3.4a16 16 0 0 0 0 4zm.8 2h3a15 15 0 0 0 1.3 4A8 8 0 0 1 5.1 16zm3-8h-3a8 8 0 0 1 4.3-4 15 15 0 0 0-1.3 4zM12 20c-.9-1.2-1.6-2.6-2-4h4c-.4 1.4-1.1 2.8-2 4zm2.3-6H9.7a14 14 0 0 1 0-4h4.6a14 14 0 0 1 0 4zm.3 6a15 15 0 0 0 1.3-4h3a8 8 0 0 1-4.3 4zm1.7-6a16 16 0 0 0 0-4h3.4a8 8 0 0 1 0 4z"/></svg>
          www.tidewellvitality.com
        </li>
      </ul>
    </div>

    <p class="address">614 Birchmoor Ave, Alderbrook Heights, MI 49307</p>
    <div class="base-band"></div>
  </section>

</body>
</html>
```